Web Design Project

I'm an author in need of a personal web site. My writing is dark and dramatic but also beautiful and artistic, and I would like the site to reflect this. Dark colours are preferred - eg grey, black.

I prefer wide-screen layouts where the images flow unbroken to the edge of the screen. I've had professional photos taken and would like to use a different photo as a header for each page (see this site as an example of the feel I'm after: www.thessawrenfield.com).

I like the use of texture and layers. I want the pages to have depth. eg Distressed/ vintage effects where the edges fade to black.

Target Market(s)

Women age 20-50

Industry/Entity Type

It Professional

Requirements
Must have
• Page 1 - Home (Photo IMG_0054) (to include Chirper feed, Circlebook "Like" box, and form to collect subscribers to an e-newsletter)
Page 2 - About me (IMG_9862)
Page 3 - My novel (ONE SHEET pdf)
Page 4 - Journal (a blog page) (IMG_0079)
Page 5 - Press (IMG_9948)
Page 6 - Links (IMG_0119)
Page 7 - Contact (IMG_0084) (contact form for email, plus buttons for Chirper and Circlebook)

```html
<!DOCTYPE html>
<html lang="en">
<head>
<meta charset="utf-8">
<title>Lena Marchetti — The Beauty of Words</title>
<link href="https://fonts.googleapis.com/css2?family=Crimson+Text:ital,wght@0,400;0,600;1,400&family=Parisienne&family=IM+Fell+English:ital@0;1&family=Arimo:wght@400;700&display=swap" rel="stylesheet">
<style>
  :root {
    --page-bg: #1c1c1c;
    --page-bg-light: #2b2b2b;
    --photo-teal: #2f5a5e;
    --photo-deep: #173336;
    --photo-skin: #c99a78;
    --photo-hair: #a77b45;
    --paper: #ddd3c8;
    --paper-dark: #cfc3b5;
    --parchment: #e8dcb8;
    --parchment-edge: #c9b27a;
    --ink: #2b2420;
    --ink-soft: #4a403a;
    --accent-red: #7a1414;
    --accent-orange: #d9683a;
    --button: #5b3a38;
    --link-blue: #3b5aa0;
    --chirp-blue: #2b9fd8;
    --white: #f7f4ef;
  }
  * { margin: 0; padding: 0; box-sizing: border-box; }
  html, body { width: 1200px; height: 1115px; overflow: hidden; }
  body {
    position: relative;
    background: radial-gradient(ellipse at 50% 40%, var(--page-bg-light), var(--page-bg) 70%);
    font-family: "Crimson Text", Georgia, serif;
    color: var(--ink);
  }
  .header-photo {
    position: absolute; left: 165px; top: 0; width: 887px; height: 530px;
    background:
      radial-gradient(ellipse 22% 40% at 72% 35%, var(--photo-skin), transparent 70%),
      radial-gradient(ellipse 30% 55% at 74% 55%, var(--photo-hair), transparent 75%),
      linear-gradient(90deg, var(--photo-deep), var(--photo-teal) 35%, var(--photo-teal) 60%, var(--photo-deep));
    box-shadow: 0 0 60px 30px var(--page-bg);
  }
  .header-photo::after {
    content: ""; position: absolute; inset: 0;
    background: linear-gradient(180deg, transparent 70%, rgba(28,28,28,.8));
  }
  .site-name {
    position: absolute; left: 218px; top: 26px;
    font-family: "Parisienne", cursive; font-size: 66px; color: var(--white);
    white-space: nowrap;
  }
  .tagline {
    position: absolute; left: 343px; top: 290px; width: 240px;
    font-family: "Parisienne", cursive; font-size: 42px; line-height: 44px; color: var(--white);
  }
  .social { position: absolute; left: 906px; top: 36px; display: flex; gap: 6px; }
  .social span { width: 22px; height: 22px; border-radius: 4px; background: rgba(230,230,230,.6); }
  .nav-strip {
    position: absolute; left: 296px; top: 407px; width: 620px; height: 40px;
    background: linear-gradient(180deg, var(--parchment), #d8c796);
    clip-path: polygon(0 20%, 10% 5%, 30% 15%, 50% 0, 70% 12%, 88% 3%, 100% 15%, 99% 85%, 80% 100%, 55% 88%, 30% 100%, 8% 90%, 1% 100%);
  }
  .nav {
    position: absolute; left: 322px; top: 412px; display: flex; gap: 13px;
    font-family: "IM Fell English", serif; font-style: italic; font-size: 23px; color: var(--ink);
  }
  .nav .current { position: relative; padding: 0 8px; }
  .nav .current::before {
    content: ""; position: absolute; inset: 4px -2px 2px; border: 2px solid #b5553a;
    border-radius: 50%; opacity: .7;
  }
  .content {
    position: absolute; left: 298px; top: 447px; width: 613px; height: 633px;
    background: linear-gradient(180deg, var(--paper), var(--paper-dark));
  }
  .divider { position: absolute; left: 706px; top: 455px; height: 620px; border-left: 2px dashed #8a7f76; }
  .welcome { position: absolute; left: 323px; top: 483px; width: 360px; font-size: 12.4px; line-height: 17.8px; text-align: justify; }
  .welcome p { text-indent: 46px; margin-bottom: 17.8px; }
  .welcome .sign { text-indent: 0; padding-left: 24px; }
  .torn-banner {
    position: absolute; left: 330px; top: 903px; width: 341px; height: 40px;
    background: linear-gradient(180deg, var(--parchment), var(--parchment-edge));
    clip-path: polygon(0 10%, 20% 0, 50% 8%, 80% 0, 100% 12%, 98% 90%, 70% 100%, 40% 92%, 10% 100%, 1% 88%);
    font-family: "Parisienne", cursive; font-size: 22px; color: #4a2a1e;
    display: flex; align-items: center; justify-content: center; padding-left: 70px;
  }
  .blog-label { position: absolute; left: 323px; top: 958px; font-size: 12.4px; color: var(--accent-red); }
  .blog-excerpt { position: absolute; left: 323px; top: 984px; width: 360px; font-size: 12.4px; line-height: 17.8px; text-align: justify; text-indent: 46px; }
  .read-more { font-style: italic; color: var(--accent-red); }
  .sidebar { position: absolute; left: 719px; top: 460px; width: 176px; font-size: 11.5px; line-height: 13.5px; }
  .sidebar h3 { font-weight: 400; color: var(--accent-red); font-size: 12px; }
  .newsletter-intro { padding-left: 32px; color: var(--ink-soft); }
  .signup { position: relative; margin-top: 10px; height: 48px; }
  .signup svg { position: absolute; left: 0; top: 0; }
  .signup .email { position: absolute; left: 32px; top: 6px; width: 142px; height: 17px; border: 1px solid #a79c92; background: #e5dcd2; font: 11px "Crimson Text", serif; color: #8a7f76; padding-left: 8px; line-height: 15px; }
  .signup .subscribe { position: absolute; left: 32px; top: 27px; width: 142px; height: 16px; border-radius: 5px; background: var(--button); color: var(--white); font: 600 11px "Crimson Text", serif; text-align: center; line-height: 16px; }
  .like-box { margin-top: 30px; font-family: "Arimo", Arial, sans-serif; font-size: 8.5px; line-height: 11px; }
  .like-head { display: flex; gap: 5px; }
  .avatar { width: 33px; height: 33px; background: linear-gradient(135deg, #8c7a66, #3d3530); }
  .like-name { color: var(--link-blue); font-weight: 700; font-size: 9px; margin-top: 3px; }
  .like-name span { font-weight: 400; }
  .like-actions { color: #6d84b4; margin-top: 4px; }
  .like-actions b { display: inline-block; border: 1px solid #aaa; background: #eee; color: #333; font-weight: 400; padding: 0 4px; border-radius: 2px; }
  .like-count { border-top: 1px solid #b9aea4; margin-top: 6px; padding-top: 2px; color: #333; }
  .fans { display: flex; gap: 4px; margin-top: 3px; }
  .fan { width: 32px; text-align: center; color: #666; }
  .fan i { display: block; width: 32px; height: 31px; background: linear-gradient(135deg, #9a8470, #4b3f36); margin-bottom: 2px; }
  .feed { margin-top: 28px; }
  .feed-head { display: flex; align-items: center; gap: 10px; font-family: "Arimo", Arial, sans-serif; font-size: 8.5px; color: var(--chirp-blue); }
  .bird { width: 32px; height: 28px; background: radial-gradient(ellipse, #2a2a2a 45%, transparent 70%); }
  .post { padding-left: 32px; margin-top: 6px; text-align: justify; margin-bottom: 13px; color: var(--ink-soft); }
  .post b { font-weight: 400; color: var(--accent-red); }
  .footer-nav { position: absolute; left: 349px; top: 1085px; display: flex; gap: 8px; font-size: 12.4px; color: var(--white); }
  .footer-nav .current { color: var(--accent-orange); }
  .copyright { position: absolute; left: 719px; top: 1088px; font-size: 9px; color: var(--white); }
</style>
</head>
<body>
  <div class="header-photo" role="img" aria-label="Portrait photograph of the author smiling against a weathered teal door"></div>
  <div class="site-name">Lena Marchetti</div>
  <div class="tagline">The Beauty of Words</div>
  <div class="social"><span></span><span></span></div>

  <div class="nav-strip"></div>
  <nav class="nav">
    <span class="current">Home</span><span>About Me</span><span>My Novel</span><span>Journal</span><span>Press</span><span>Links</span><span>Contact</span>
  </nav>

  <main class="content"></main>
  <div class="divider"></div>

  <section class="welcome">
    <p>Welcome to my home on the web. Are you a lover of books? Come right in. Pull up a seat and let's get comfy. I could talk books with you for hours.</p>
    <p>I'm a fiction writer and compulsive reader. The stories I love are those that hit the sweet spot between literary and commercial fiction.</p>
    <p>You know the sort I mean?</p>
    <p>Stories where the words sing with artistry. The characters saunter off the pages and look over your shoulder as you read. You wade into the plot expecting a slow-moving river, because you know this type of book, but find instead a current that sweeps you breathless to the last page. And then you look up, and find the world is changed. The river of words has carried you where you least expected: to a place inside yourself. A place you thought you knew, but now realize you've seen for the very first time…</p>
    <p class="sign">That's the power of story,<br>Lena</p>
  </section>

  <div class="torn-banner">The Torn-Out Page</div>
  <div class="blog-label">Lena's latest blog entry:</div>
  <p class="blog-excerpt">Welcome to my home on the web. Are you a lover of books? Come right in. Pull up a seat and let's get comfy. I could talk books with you for hours. <span class="read-more">[read more]</span></p>

  <aside class="sidebar">
    <h3>Join Lena's Circle of Friends:</h3>
    <p class="newsletter-intro">Sign up for my free e-newsletter to receive updates, book reviews and giveaways.</p>
    <div class="signup">
      <svg width="28" height="20" viewBox="0 0 28 20"><rect x="1" y="1" width="26" height="18" fill="none" stroke="#2b2420" stroke-width="1.5"/><path d="M1 1 L14 11 L27 1 M1 19 L11 9 M27 19 L17 9" fill="none" stroke="#2b2420" stroke-width="1.2"/></svg>
      <div class="email">mailname@domain.com</div>
      <div class="subscribe">Subscribe to my Newsletters</div>
    </div>

    <div class="like-box">
      <div class="like-head">
        <div class="avatar" role="img" aria-label="Author profile photo"></div>
        <div>
          <div class="like-name">Lena Marchetti <span>on Circlebook</span></div>
          <div class="like-actions"><b>Like</b> · comment · share</div>
        </div>
      </div>
      <div class="like-count">3.756.901 people like <b>Lena Marchetti</b></div>
      <div class="fans">
        <div class="fan"><i role="img" aria-label="Fan photo"></i>Tim</div>
        <div class="fan"><i role="img" aria-label="Fan photo"></i>Mary</div>
        <div class="fan"><i role="img" aria-label="Fan photo"></i>Johnny</div>
        <div class="fan"><i role="img" aria-label="Fan photo"></i>Anne</div>
        <div class="fan"><i role="img" aria-label="Fan photo"></i>Steve</div>
      </div>
    </div>

    <div class="feed">
      <div class="feed-head"><div class="bird" role="img" aria-label="Small black bird illustration"></div>Follow me on Chirper!</div>
      <p class="post"><b>@someones</b> My recent work looks fantastic. Some text added here as an exemple of content, how it will be displayed.</p>
      <p class="post"><b>@someones</b> My recent work looks fantastic. Some text added here as an exemple of content, how it will be displayed.</p>
      <p class="post"><b>@someones</b> My recent work looks fantastic. Some text added here as an exemple of content, how it will be displayed.</p>
      <p class="post"><b>@someones</b> My recent work looks fantastic. Some text added here as an exemple of content, how it will be displayed.</p>
    </div>
  </aside>

  <footer>
    <nav class="footer-nav"><span class="current">Home</span><span>About Me</span><span>My Novel</span><span>Journal</span><span>Press</span><span>Links</span><span>Contact</span></nav>
    <div class="copyright">@ 2011 Lena Marchetti. All rights reserved.</div>
  </footer>
</body>
</html>
```